Weight Loss Banner Ad

We need banner ads for our website, www.bluvantaplan.com. We would like to see Banner ads that represent what you think is the most captivating aspect of The Bluvanta Plan. Please review the website.

The banner ad should be something you REALLY want to click on. It needs to include the name and/or logo and the slogan "Gourmet Meals Direct To Your House"

We will want the final ad in multiple sizes but it should use the same image and copy.

Logo is attached, so are images. Feel free to use your own if you think you have a better on

Size (pixels):
468 x 60
392 x 72
234 x 60
125 x 125
120 x 90
120 x 60
88 x 31
120 x 240
120 x 600
160 x 600

Target Market(s)

Fitness Enthusiast looking to lose weight.

Industry/Entity Type

Weight

Font styles to use
Sans Serif

Requirements
Must have
• See Description
Nice to have
• Should be awesome and make you want to buy some food. Also you may want to say something about the price:

i.e. Starting at only $99

```html
<!DOCTYPE html>
<html lang="en">
<head>
<meta charset="utf-8">
<title>The Bluvanta Plan – Banner Set</title>
<link rel="stylesheet" href="https://fonts.googleapis.com/css2?family=Open+Sans:wght@400;600;700&display=swap">
<style>
  :root {
    --backdrop: #a9cbd1;
    --paper: #ffffff;
    --brand-green: #8dc63f;
    --btn-top: #a6d64a;
    --btn-bottom: #6aa51c;
    --btn-edge: #5a8f16;
    --ink: #111111;
    --meat-dark: #4a1f1a;
    --meat-mid: #7a3a2c;
    --plate: #f1efec;
  }
  * { box-sizing: border-box; margin: 0; padding: 0; }
  html, body { width: 1200px; height: 847px; overflow: hidden; }
  body {
    background: var(--backdrop);
    font-family: "Open Sans", Arial, sans-serif;
    position: relative;
  }
  .banner {
    position: absolute;
    background: var(--paper);
    overflow: hidden;
    box-shadow: 2px 3px 6px rgba(0,0,0,.28);
  }
  .brand {
    position: absolute;
    z-index: 2;
    color: var(--brand-green);
    font-weight: 700;
    line-height: 1.05;
    white-space: nowrap;
  }
  .food-photo {
    position: absolute;
    z-index: 1;
    background:
      radial-gradient(ellipse 45% 38% at 50% 48%, var(--meat-mid) 0%, var(--meat-dark) 60%, transparent 75%),
      linear-gradient(180deg, #ffffff 0%, #f4f1ee 55%, var(--plate) 100%);
  }
  .photo-wide {
    background:
      radial-gradient(ellipse 32% 45% at 50% 50%, var(--meat-mid) 0%, var(--meat-dark) 60%, transparent 78%),
      linear-gradient(90deg, #ffffff 0%, #efebe7 100%);
  }
  .cta {
    position: absolute;
    z-index: 3;
    display: flex; align-items: center; justify-content: center;
    background: linear-gradient(180deg, var(--btn-top), var(--btn-bottom));
    border: 1px solid var(--btn-edge);
    border-radius: 3px;
    color: #1d2a08;
    font-weight: 400;
    box-shadow: 0 2px 3px rgba(0,0,0,.3);
  }
  .copy { position: absolute; z-index: 2; text-align: center; color: var(--ink); line-height: 1.15; white-space: nowrap; }
  .copy b { font-weight: 700; }
  .copy .green { color: var(--brand-green); font-weight: 700; }
  .ribbon {
    position: absolute;
    z-index: 2;
    background: var(--brand-green);
    color: #fff;
    font-size: 20px;
    line-height: 1;
  }
  .ribbon-right {
    clip-path: polygon(0 0, 82% 0, 100% 50%, 82% 100%, 0 100%);
    padding: 5px 0 0 10px;
  }
  .ribbon-left {
    clip-path: polygon(18% 0, 100% 0, 100% 100%, 18% 100%, 0 50%);
    padding: 8px 10px 0 0; text-align: right; font-size: 17px;
  }
  .green-band {
    position: absolute; left: 0; right: 0; bottom: 0; z-index: 2;
    background: var(--brand-green); color: #fff; text-align: center;
    font-size: 10.5px; line-height: 1.1; padding-top: 2px;
  }
</style>
</head>
<body>

<!-- 160 x 600 ribbon skyscraper -->
<section class="banner" style="left:131px;top:71px;width:167px;height:624px">
  <span class="brand" style="left:10px;top:18px;font-size:17px">The Bluvanta<br>Plan</span>
  <div class="ribbon ribbon-right" style="left:0;top:175px;width:139px;height:52px">Gourmet<br>Meals</div>
  <div class="ribbon ribbon-left" style="left:21px;top:242px;width:146px;height:55px">Direct To<br><b>Your House</b></div>
  <div class="food-photo" role="img" aria-label="Close-up of a seasoned, herb-crusted steak on a white plate with grilled vegetables" style="left:0;top:300px;width:167px;height:260px"></div>
  <div class="cta" style="left:16px;top:579px;width:130px;height:33px;font-size:13px">VISIT NOW</div>
</section>

<!-- 160 x 600 stacked-copy skyscraper -->
<section class="banner" style="left:311px;top:71px;width:167px;height:624px">
  <span class="brand" style="left:8px;top:22px;font-size:21px">The Bluvanta<br>Plan</span>
  <div class="copy" style="left:0;right:0;top:173px;font-size:17px">
    <span class="green" style="font-size:23px">Gourmet<br>Meals</span><br>Direct To<br><b>Your House</b>
  </div>
  <div class="food-photo" role="img" aria-label="Close-up of a seasoned, herb-crusted steak on a white plate with grilled vegetables" style="left:0;top:300px;width:167px;height:260px"></div>
  <div class="cta" style="left:21px;top:579px;width:130px;height:33px;font-size:13px">VISIT NOW</div>
</section>

<!-- 234 x 60 -->
<section class="banner" style="left:497px;top:284px;width:244px;height:61px">
  <span class="brand" style="left:8px;top:9px;font-size:12px">The Bluvanta Plan</span>
  <div class="food-photo photo-wide" role="img" aria-label="Rack of lamb with roasted vegetables on a plate" style="left:124px;top:0;width:120px;height:36px"></div>
  <div class="copy" style="left:0;right:0;top:38px;font-size:11.5px"><b>Gourmet Meals Direct To Your House</b></div>
</section>

<!-- 120 x 240 black copy -->
<section class="banner" style="left:492px;top:367px;width:125px;height:250px">
  <span class="brand" style="left:8px;top:14px;font-size:15px">The Bluvanta<br>Plan</span>
  <div class="copy" style="left:0;right:0;top:82px;font-size:11.5px"><b>Gourmet Meals</b><br>Direct To<br><b>Your House!</b></div>
  <div class="food-photo" role="img" aria-label="Rack of lamb with roasted vegetables on a plate" style="left:0;top:135px;width:125px;height:80px"></div>
  <div class="cta" style="left:13px;top:218px;width:100px;height:24px;font-size:10.5px">VISIT NOW</div>
</section>

<!-- 120 x 240 green copy -->
<section class="banner" style="left:630px;top:367px;width:125px;height:250px">
  <span class="brand" style="left:8px;top:14px;font-size:15px">The Bluvanta<br>Plan</span>
  <div class="copy" style="left:0;right:0;top:82px;font-size:11.5px"><span class="green">Gourmet Meals</span><br>Direct To<br>Your House!</div>
  <div class="food-photo" role="img" aria-label="Rack of lamb with roasted vegetables on a plate" style="left:0;top:135px;width:125px;height:80px"></div>
  <div class="cta" style="left:13px;top:218px;width:100px;height:24px;font-size:10.5px">VISIT NOW</div>
</section>

<!-- 125 x 125 -->
<section class="banner" style="left:769px;top:383px;width:130px;height:130px">
  <span class="brand" style="left:14px;top:8px;font-size:15px">The Bluvanta<br>Plan</span>
  <div class="food-photo" role="img" aria-label="Rack of lamb with roasted vegetables on a plate" style="left:20px;top:44px;width:95px;height:48px"></div>
  <div class="copy" style="left:0;right:0;top:95px;font-size:10.5px"><b>Gourmet Meals</b><br><span style="font-size:9.5px;font-weight:600">Direct To Your House</span></div>
</section>

<!-- 120 x 60 -->
<section class="banner" style="left:771px;top:527px;width:125px;height:62px">
  <span class="brand" style="left:10px;top:8px;font-size:11px">The Bluvanta Plan</span>
  <div class="green-band" style="height:27px">Gourmet Meals<br>Direct To Your House</div>
</section>

<!-- 120 x 90 -->
<section class="banner" style="left:771px;top:602px;width:125px;height:94px">
  <span class="brand" style="left:6px;top:8px;font-size:12px">The Bluvanta<br>Plan</span>
  <div class="food-photo" role="img" aria-label="Rack of lamb with roasted vegetables on a plate" style="left:82px;top:6px;width:43px;height:56px"></div>
  <div class="copy" style="left:0;right:0;top:66px;font-size:9.5px"><b>Gourmet Meals</b><br><span style="font-size:8.5px;font-weight:600">Direct To Your House</span></div>
</section>

<!-- 88 x 31 -->
<section class="banner" style="left:910px;top:664px;width:92px;height:32px">
  <span class="brand" style="left:3px;top:10px;font-size:8.5px">The Bluvanta</span>
  <div class="food-photo photo-wide" role="img" aria-label="Plated gourmet meat dish" style="left:62px;top:0;width:30px;height:32px"></div>
</section>

<!-- 234 x 60 (two-line) -->
<section class="banner" style="left:492px;top:633px;width:244px;height:62px">
  <span class="brand" style="left:6px;top:8px;font-size:12.5px">The Bluvanta Plan</span>
  <div class="copy" style="left:4px;top:36px;text-align:left;font-size:10.5px"><b>Gourmet Meals<br>Direct To Your House</b></div>
  <div class="food-photo photo-wide" role="img" aria-label="Rack of lamb with roasted vegetables on a plate" style="left:126px;top:0;width:118px;height:62px"></div>
</section>

<!-- 468 x 60 -->
<section class="banner" style="left:131px;top:709px;width:488px;height:62px">
  <span class="brand" style="left:8px;top:14px;font-size:17px">The Bluvanta<br>Plan</span>
  <div class="copy" style="left:120px;width:120px;top:11px;font-size:12.5px"><b>Gourmet Meals</b><br>Direct To<br><b>Your House</b></div>
  <div class="food-photo photo-wide" role="img" aria-label="Herb-crusted steak with grilled vegetables on a plate" style="left:245px;top:0;width:100px;height:62px"></div>
  <div class="cta" style="left:347px;top:17px;width:130px;height:33px;font-size:13px">VISIT NOW</div>
</section>

<!-- 392 x 72 -->
<section class="banner" style="left:630px;top:709px;width:408px;height:75px">
  <span class="brand" style="left:14px;top:16px;font-size:19px">The Bluvanta<br>Plan</span>
  <div class="food-photo photo-wide" role="img" aria-label="Herb-crusted steak with grilled vegetables on a plate" style="left:150px;top:0;width:100px;height:75px"></div>
  <div class="copy" style="left:254px;width:150px;top:6px;font-size:11.5px"><b style="font-size:12.5px">Gourmet Meals</b><br><b>Direct To Your House!</b></div>
  <div class="cta" style="left:268px;top:38px;width:130px;height:31px;font-size:13px">VISIT NOW</div>
</section>

</body>
</html>
```